Glowline Tube Works Mailer / Flyer

Create a visually engaging, print-ready brochure that effectively highlights Glowline Tube Works’s services, repair process, sales, and event opportunities while reflecting the bold, eye-catching aesthetics of neon signage. The brochure should be easy to read, well-structured, and convey our commitment to preserving vintage neon. It will serve as both a marketing piece for potential customers and a take-home reference for people interested in repairs, sales, or events.

Target Market(s)

Bar Owners & Business Owners with neon signs. Collectors & Enthusiasts of vintage beer and advertising neon signs. Neon Sign Repair Technicians & Shops who want to focus on custom work instead of repairs. Homeowners & Hobbyists with neon signs in need of repair. Vendors & Sellers who want to participate in Hopvale Tap Fairs & Pop-Up Sales.

Industry/Entity Type

Vintage Neon Signs, Restoration, and Collectibles

Font styles to use
Sans Serif

Colors
59FF00
82FF00
B8FF75
E3FFCB
F4FFEA
EB3D1F
EC4F4E
F09395
F8D3D4
FCEDEE

Requirements
Must have
• ✔ Bold, neon-inspired design that stands out and reflects vintage neon culture. ✔ Clear, structured sections detailing: Neon sign sales & replacement parts Repair & cleaning services Buying & trading neon signs Pickup & delivery routes & scheduling Custom neon sign information Open Houses & Hopvale Tap Fair event details ✔ Contact Information: info@glowlinetubeworks.example + website & location. ✔ Call-to-action prompts for potential customers (e.g., “Get on Our Pickup Schedule Today!”). QR CODE
Nice to have
• 💡 Vintage-style graphics or textures that resemble old neon advertising. 💡 A side-by-side comparison of traditional neon vs. LED to educate customers. 💡 A nostalgic touch—highlighting how neon signs have sentimental value (e.g., a bar owner’s family-owned neon sign). 💡 Customer testimonials or a short ‘Our Story’ section about how Glowline Tube Works started.
Should not have
• ❌ No cluttered or overly busy design—the information must be clear and easy to scan. ❌ No LED promotion—we specialize in true neon, not LED knock-offs. ❌ No overly modern or sleek design—the style should reflect the vintage neon aesthetic. ❌ No generic stock images—use authentic neon sign photography that represents our work.

```html
<!DOCTYPE html>
<html lang="en">
<head>
<meta charset="utf-8">
<title>Glowline Tube Works – Brochure Front</title>
<link rel="stylesheet" href="https://fonts.googleapis.com/css2?family=Rubik:ital,wght@0,400;0,500;0,600;0,700;0,800;1,700&family=Manrope:wght@300;400;500;600;700&family=Sacramento&family=Yellowtail&display=swap">
<style>
  :root{
    --page-top:#0b0b0b;
    --page-bottom:#1c1c1c;
    --panel:#161616;
    --panel-edge:#f2f2f2;
    --card:#0c0c0c;
    --white:#ffffff;
    --soft:#e6e6e6;
    --green:#1ed760;
    --green-deep:#00c04b;
    --lime:#b8ff75;
    --pink:#ff1f6e;
    --pink-soft:#f09395;
    --cyan:#36d8f5;
    --yellow:#ffe33a;
  }
  *{box-sizing:border-box;margin:0;padding:0}
  html,body{width:1153px;height:1200px;overflow:hidden}
  body{
    background:linear-gradient(180deg,var(--page-top) 0%,#151515 55%,var(--page-bottom) 100%);
    font-family:"Manrope",sans-serif;color:var(--white);position:relative;
  }
  .side-label{
    position:absolute;top:28px;left:0;width:100%;text-align:center;
    font-family:"Rubik",sans-serif;font-weight:600;font-size:46px;letter-spacing:.5px;
  }
  .brochure{
    position:absolute;left:60px;top:112px;width:1033px;height:798px;
    border:1.5px solid var(--panel-edge);overflow:hidden;
    background:radial-gradient(ellipse at 50% 40%,#262626 0%,var(--panel) 60%,#0e0e0e 100%);
  }
  .cables{position:absolute;inset:0;width:100%;height:100%}
  .abs{position:absolute}

  /* left panel */
  .brand-name{
    left:30px;top:170px;width:300px;
    font-family:"Rubik",sans-serif;font-weight:800;font-size:38px;line-height:42px;
    color:var(--green);display:flex;align-items:center;gap:12px;
  }
  .brand-name .dot{width:16px;height:16px;border-radius:50%;background:var(--green);flex:none}
  .legacy-dot{left:40px;top:351px;width:15px;height:15px;border-radius:50%;
    background:var(--lime);box-shadow:0 0 8px var(--green),0 0 2px #fff}
  .legacy-title{left:69px;top:336px;font-family:"Rubik",sans-serif;font-weight:600;font-size:18px;line-height:21.5px}
  .legacy-title .pink{color:var(--pink)}
  .legacy-title .green{color:var(--green)}
  .legacy-rule{left:45px;top:405px;width:4px;height:153px;border-radius:2px;
    background:var(--pink);box-shadow:0 0 6px var(--pink)}
  .about{left:69px;top:402px;width:250px;font-size:13.5px;line-height:18.4px;font-weight:400;color:var(--soft)}
  .about p+p{margin-top:11.5px}
  .hl-green{background:var(--green-deep);color:#fff;border-radius:4px;padding:0 2px}
  .hl-pink{background:var(--pink);color:#fff;border-radius:4px;padding:0 2px}
  .led-note{
    left:20px;top:627px;width:305px;text-align:center;
    font-family:"Rubik",sans-serif;font-weight:700;font-size:18.5px;line-height:23.6px;letter-spacing:.3px;
  }
  .led-note .g{color:var(--green);text-shadow:0 0 6px rgba(30,215,96,.7)}
  .led-note .p{color:var(--pink);text-shadow:0 0 6px rgba(255,31,110,.7)}

  /* middle panel */
  .offer-script{left:395px;top:8px;width:250px;text-align:center;white-space:nowrap;
    font-family:"Sacramento",cursive;font-size:84px;line-height:100px;color:var(--cyan);
    text-shadow:0 0 8px rgba(54,216,245,.8)}
  .offer-word{left:491px;top:108px;font-family:"Rubik",sans-serif;font-style:italic;font-weight:700;
    font-size:30px;line-height:34px;letter-spacing:2.5px;color:var(--yellow);transform:rotate(-4deg);
    text-shadow:0 0 8px rgba(255,227,58,.55)}
  .service-icon{width:46px;height:46px}
  .service-title{left:429px;font-family:"Rubik",sans-serif;font-weight:600;font-size:13.6px;line-height:17.7px}
  .service-title .yellow{color:var(--yellow)}
  .service-title .cyan{color:var(--cyan)}
  .service-card{left:387px;width:282px;padding:6px 8px 7px 11px;background:var(--card);border-radius:10px 0 0 10px;
    font-size:11.6px;line-height:16px;color:#d9d9d9}
  .service-card p+p{margin-top:9.5px}
  .service-card b{font-weight:700;color:#fff}

  /* right panel */
  .truck-art{left:760px;top:75px;width:223px;height:148px;border-radius:18px;
    background:radial-gradient(ellipse at center,rgba(30,215,96,.55) 0%,rgba(30,215,96,.22) 55%,rgba(30,215,96,0) 75%)}
  .pickup-script{left:735px;top:232px;width:260px;text-align:center;white-space:nowrap;
    font-family:"Yellowtail",cursive;font-size:36px;line-height:42px;
    color:var(--pink);transform:rotate(-8deg);text-shadow:0 0 8px rgba(255,31,110,.7)}
  .services-word{left:797px;top:278px;width:170px;text-align:center;white-space:nowrap;
    font-family:"Rubik",sans-serif;font-weight:600;font-size:25px;line-height:30px;letter-spacing:2px;
    color:var(--green);transform:rotate(-8deg);text-shadow:0 0 8px rgba(30,215,96,.7)}
  .routes{left:746px;top:355px;width:230px;font-family:"Rubik",sans-serif;font-weight:500;font-size:13.6px;line-height:15.8px;letter-spacing:.2px}
  .routes .pink{color:var(--pink-soft)}
  .routes .green{color:var(--lime)}
  .routes-rule{left:746px;top:445px;width:229px;height:2px;background:#fff}
  .pill{left:751px;width:216px;border-radius:12px;display:flex;align-items:center;justify-content:center;text-align:center;
    font-family:"Rubik",sans-serif;font-weight:700;font-size:12.8px;line-height:15.8px;color:#fff;padding:0 10px}
  .pill.green{background:var(--green-deep)}
  .pill.pink{background:var(--pink)}
  .phone-icon{left:733px;top:678px;width:40px;height:40px}
  .pickup-contact{left:789px;top:664px;width:200px;font-size:13.2px;line-height:15.8px;color:#f0f0f0}
  .pickup-contact b{font-weight:700;color:#fff}

  .caption{position:absolute;top:1038px;left:0;width:100%;text-align:center;
    font-family:"Manrope",sans-serif;font-weight:400;font-size:25px;line-height:33px;color:#f2f2f2}
</style>
</head>
<body>
  <div class="side-label">Front</div>

  <section class="brochure" aria-label="Brochure front spread">
    <svg class="cables" viewBox="0 0 1033 798" aria-hidden="true">
      <path d="M600 0 C650 25 700 40 760 25 S900 70 1033 45" fill="none" stroke="#1f3a2a" stroke-width="4"/>
      <path d="M0 640 C30 680 40 720 90 740 S150 780 170 798" fill="none" stroke="#1f3a2a" stroke-width="4"/>
    </svg>

    <!-- left panel -->
    <div class="abs brand-name"><span class="dot"></span><span>Glowline Tube Works</span></div>

    <span class="abs legacy-dot"></span>
    <h2 class="abs legacy-title"><span class="pink">Preserving the</span><br><span class="green">Legacy of Neon Signs</span></h2>
    <span class="abs legacy-rule"></span>
    <div class="abs about">
      <p>Glowline Tube Works is a family-owned business specializing in <span class="hl-green">vintage neon signs and replacement parts.</span></p>
      <p>We house one of the largest inventories of new and used neon tubes available online and offer <span class="hl-pink">over 200 authentic distributor</span> neon signs and custom pieces for sale.</p>
    </div>
    <p class="abs led-note"><span class="g">We</span> <span class="p">do not sell</span> <span class="g">or</span> <span class="p">repair</span><br><span class="p">knock-off</span> <span class="g">versions</span> <span class="p">or</span><br><span class="p">next-generation LED neons.</span></p>

    <!-- middle panel -->
    <div class="abs offer-script">What We</div>
    <div class="abs offer-word">OFFER:</div>

    <svg class="abs service-icon" style="left:372px;top:168px" viewBox="0 0 46 46" aria-label="Cart icon" role="img">
      <g fill="none" stroke="#ffe33a" stroke-width="2.6" stroke-linecap="round" stroke-linejoin="round">
        <path d="M2 6h7l5 24h25l4-17H11"/>
        <path d="M15 18h27M16 24h24M22 13v17M30 13v17"/>
        <circle cx="18" cy="37" r="3.5"/><circle cx="35" cy="37" r="3.5"/>
      </g>
    </svg>
    <h3 class="abs service-title" style="top:177px">Neon Sign <span class="yellow">Sales &amp;<br>Replacement Parts</span></h3>
    <div class="abs service-card" style="top:218px">
      <p><b>One of the largest selections</b> of neon replacement tubes, transformers, tube supports, wiring, power supplies, and more.</p>
      <p><b>Authentic neon signs</b> perfect for bars, home décor, businesses, and collectors.</p>
      <p><b>Shipping available</b> for neon parts (we do not ship full signs).</p>
    </div>

    <svg class="abs service-icon" style="left:374px;top:375px" viewBox="0 0 46 46" aria-label="Tools icon" role="img">
      <g fill="none" stroke="#36d8f5" stroke-width="2.6" stroke-linecap="round" stroke-linejoin="round">
        <path d="M6 6l6 2 22 22 5 1 4 6-4 4-6-4-1-5L10 10z"/>
        <path d="M38 4a8 8 0 0 0-9 11L6 36l4 4 21-23a8 8 0 0 0 11-9l-5 4-4-1-1-4z"/>
      </g>
    </svg>
    <h3 class="abs service-title" style="top:379px">Neon Sign <span class="cyan">Repair &amp;<br>Assessment</span></h3>
    <div class="abs service-card" style="top:420px">
      <p><b>Basic Repairs:</b> Transformer swaps, wiring fixes, broken tube replacement.</p>
      <p><b>Deep Cleaning:</b> Disassemble, clean, and reassemble neon signs (inherent risks involved).</p>
      <p><b>Budget-Friendly Estimate:</b> Most basic repairs start around $150</p>
    </div>

    <svg class="abs service-icon" style="left:372px;top:577px" viewBox="0 0 46 46" aria-label="Trade arrows icon" role="img">
      <g fill="none" stroke="#ffe33a" stroke-width="2.6" stroke-linejoin="round">
        <path d="M8 16h24V10l11 9-11 9v-6H8z"/>
        <path d="M38 26H14v-6L3 29l11 9v-6h24z"/>
      </g>
    </svg>
    <h3 class="abs service-title" style="top:580px"><span class="yellow">Buying &amp; Trading</span><br>Neon Signs</h3>
    <div class="abs service-card" style="top:621px">
      <p><b>Got old neon signs taking up space?</b> We buy, repair, or repurpose vintage neon signs.</p>
      <p><b>Trade option available:</b> Repair a few of your signs in exchange for others.</p>
      <p><b>Not sure what to do?</b> Let us assess your sign and provide options.</p>
    </div>

    <!-- right panel -->
    <div class="abs truck-art" role="img" aria-label="Green neon delivery truck loaded with boxes"></div>
    <div class="abs pickup-script">Pickup &amp; Delivery</div>
    <div class="abs services-word">SERVICES</div>

    <p class="abs routes">We offer <span class="pink">scheduled pickup</span> and delivery routes every 4-6 weeks between <span class="green">Chicago, Green Bay, and Minneapolis</span> (with future expansions based on demand).</p>
    <span class="abs routes-rule"></span>

    <div class="abs pill green" style="top:471px;height:29px">FREE pickup for 5+ signs</div>
    <div class="abs pill pink" style="top:508px;height:48px">$75 pickup/delivery fee<br>for fewer than 5 signs</div>
    <div class="abs pill green" style="top:562px;height:65px">No obligation after assessment—choose repair, sale, or return</div>

    <svg class="abs phone-icon" viewBox="0 0 40 40" aria-label="Phone icon" role="img">
      <g fill="none" stroke="#ff1f6e" stroke-width="2.6" stroke-linecap="round" stroke-linejoin="round">
        <path d="M9 5l6 7-3 4c2 5 6 9 11 11l4-3 7 6-4 5C18 35 5 22 4 10z"/>
        <path d="M23 9a9 9 0 0 1 8 8M24 3a15 15 0 0 1 13 13"/>
      </g>
    </svg>
    <p class="abs pickup-contact">To get on our pickup list, <b>contact us</b> with your name, address, phone number, and estimated number of signs.</p>
  </section>

  <p class="caption">The back cover of the brochure will be designed<br>very quickly after the design style is approved and<br>.found satisfactory by you</p>
</body>
</html>
```